Introduction:
We are an Australia-based Cyber Security Penetration testing company seeking a website redesign to showcase our services, expertise, and experience. Our target audience includes businesses and organizations of all sizes who are seeking to secure their IT infrastructure against cyber threats. The purpose of the website redesign is to increase our online presence, generate leads, and establish our company as a trusted authority in the industry.
Objectives:
Create a professional and modern website that is easy to navigate and user-friendly.
Provide information about our company, services, and expertise.
Clearly display table of our 3 services: Bug Bounty as a Service, Penetration Testing and Code Review.
Generate leads through online contact forms and calls-to-action.
Optimize the website for search engines to increase visibility and traffic.
Website similar to: https://www.velmora.com.au/.
Target Audience:
Our target audience includes businesses and organizations of all sizes that require cybersecurity penetration testing services. These include:
Small and medium-sized enterprises (SMEs)
Australian Government agencies
Design Requirements:
Clean, modern, and professional design.
Use of colors that convey trust, reliability, and expertise (such as orange and grey).
Calls-to-action that encourage visitors to contact us or request a quote.
Integration with social media channels to increase engagement and brand awareness.
A blog section to showcase our thought leadership and expertise.
A news section to share updates about our company and the industry.
Content Requirements:
Home page that introduces our company and services and highlights our expertise.
About Us page that provides information about our company, team, and values.
Services page that lists our services and explains the benefits of each.
Case Studies page that showcases our previous work and success stories.
Contact Us page that includes a contact form, phone number, and email address.
Blog section with articles related to the cybersecurity industry and our services.
News section with updates about our company and the industry.

```html
<!DOCTYPE html>
<html lang="en">
<head>
<meta charset="utf-8">
<title>Cindervault — Cyber Security</title>
<link rel="stylesheet" href="https://fonts.googleapis.com/css2?family=Ubuntu:wght@500;700&family=Lato:wght@400;700&display=swap">
<style>
:root{
  --orange:#f26b3a;
  --orange-dark:#e0582a;
  --grey:#4d4e53;
  --navy:#0e2436;
  --ink:#1d1d1f;
  --muted:#8a8a8e;
  --white:#ffffff;
  --field:#f2f2f2;
  --black:#000000;
}
*{box-sizing:border-box;margin:0;padding:0}
html,body{width:1200px;height:5324px;overflow:hidden}
body{font-family:'Lato',sans-serif;color:var(--ink);background:var(--white);position:relative}
.abs{position:absolute}
h1,h2,h3,.heading{font-family:'Ubuntu',sans-serif;font-weight:700}
.top-line{position:absolute;left:0;top:0;width:1200px;height:4px;background:var(--orange)}

/* buttons */
.btn{position:absolute;display:flex;align-items:center;justify-content:space-between;height:46px;border-radius:23px;padding:0 8px 0 20px;font-size:15px;font-weight:700;text-decoration:none}
.btn-orange{background:var(--orange);color:var(--white)}
.btn-white{background:var(--white);color:var(--orange)}
.btn-white.dark{color:#555}
.btn .dot{width:32px;height:32px;border-radius:50%;border:3px solid currentColor;display:flex;align-items:center;justify-content:center;margin-left:12px}
.btn-white .dot{color:var(--orange)}
.btn .dot svg{width:14px;height:14px}

/* header */
.site-header{position:absolute;left:0;top:4px;width:1200px;height:141px;background:var(--white)}
.brand{position:absolute;display:flex;align-items:center;gap:12px;font-family:'Ubuntu',sans-serif;font-weight:700;color:var(--orange)}
.brand .mark{border-radius:50%;background:var(--orange)}
.main-nav a{position:absolute;top:96px;font-size:16px;color:#333;text-decoration:none}

/* hero */
.hero{position:absolute;left:0;top:145px;width:1200px;height:600px;background:linear-gradient(100deg,#0a1a28 0%,#123048 55%,#0d2a44 100%)}
.hero-art{position:absolute;left:660px;top:0;width:540px;height:600px;background:radial-gradient(circle at 55% 45%,#2a6a8a 0%,#174060 35%,rgba(13,42,68,0) 70%)}
.hero h1.small{position:absolute;left:110px;top:115px;font-size:58px;color:var(--white);line-height:1}
.hero h1.big{position:absolute;left:110px;top:182px;font-size:90px;color:var(--white);line-height:1}
.hero p{position:absolute;left:110px;top:305px;width:470px;font-size:20px;line-height:34px;color:var(--white)}

/* contact cloud */
.contact-cloud{position:absolute;left:690px;top:585px;width:410px;height:290px}
.contact-cloud .label{position:absolute;left:0;top:178px;width:100%;text-align:center;font-family:'Ubuntu',sans-serif;font-weight:700;font-size:36px;color:var(--white)}

/* about */
.about-photo{position:absolute;left:122px;top:970px;width:454px;height:454px;border-radius:50%;background:radial-gradient(circle at 40% 40%,#5a4a48 0%,#2e2c30 55%,#17191d 100%)}
.about h2{position:absolute;left:620px;top:985px;font-size:66px;color:var(--ink)}
.about h2 span,.sec-title span{color:var(--orange)}
.about p{position:absolute;left:620px;top:1080px;width:470px;font-size:17px;line-height:35px;color:#666}

/* section titles */
.sec-title{position:absolute;left:0;width:1200px;text-align:center;font-size:60px;line-height:1}
.sec-sub{position:absolute;left:200px;width:800px;text-align:center;font-size:14.5px;line-height:29px}

/* services */
.services{position:absolute;left:0;top:1547px;width:1200px;height:792px;background:linear-gradient(180deg,#55565b,#46474c)}
.services .sec-title,.services .sec-sub{color:var(--white)}
.service-card{position:absolute;top:285px;width:312px;height:380px;border-radius:16px;background:var(--white);border:4px solid var(--white);overflow:hidden}
.service-card.featured{background:var(--orange)}
.service-card .thumb{height:196px;border-radius:12px 12px 0 0}
.service-card h3{margin-top:26px;text-align:center;font-size:23px;color:var(--ink)}
.service-card p{margin:14px auto 0;width:250px;text-align:center;font-size:13px;line-height:21px;color:#888}
.service-card.featured h3,.service-card.featured p{color:var(--white)}

/* blogs */
.blog-grid{position:absolute;left:110px;top:2637px;width:978px;height:420px;background:var(--white);box-shadow:0 0 10px rgba(0,0,0,.18)}
.blog-col{position:absolute;top:6px;width:320px;height:408px}
.blog-img{position:absolute;left:0;width:320px;height:212px}
.tag{position:absolute;background:var(--orange);color:var(--white);font-size:12px;font-weight:700;padding:8px 16px}
.blog-col h3{position:absolute;left:26px;width:280px;font-family:'Lato',sans-serif;font-weight:700;font-size:15.5px;line-height:25px}
.blog-col p{position:absolute;left:26px;width:280px;font-size:12px;line-height:22px;color:#888}
.blog-col a{position:absolute;left:26px;font-size:11px;font-weight:700;color:var(--orange)}
.notch{position:absolute;width:0;height:0;border-left:20px solid transparent;border-right:20px solid transparent}

/* contact form */
.touch{position:absolute;left:0;top:3259px;width:1200px;height:748px;background:linear-gradient(180deg,#f2703f,#ee6434)}
.touch .sec-title,.touch .sec-sub{color:var(--white)}
.field-label{position:absolute;font-size:14px;color:var(--white)}
.field{position:absolute;background:var(--field);border:1px solid #e2e2e2;font-size:14px;color:#666;padding:0 18px;display:flex;align-items:center}
.field.area{align-items:flex-start;padding-top:14px}

/* news */
.news-card{position:absolute;top:4285px;width:314px;height:395px;border-radius:10px;background:var(--white);box-shadow:0 0 10px rgba(0,0,0,.15);overflow:hidden}
.news-card .thumb{margin:6px 6px 0;height:194px;border-radius:6px 6px 0 0}
.news-card h3{margin:30px auto 0;width:250px;text-align:center;font-family:'Lato',sans-serif;font-weight:700;font-size:15px;line-height:23px}
.news-card p{margin:10px auto 0;width:250px;text-align:center;font-size:12.5px;line-height:21.5px;color:#888}
.news-card .meta{position:absolute;left:48px;right:48px;bottom:22px;display:flex;justify-content:space-between;font-size:12px}

/* footer */
.site-footer{position:absolute;left:0;top:4890px;width:1200px;height:434px;background:var(--black);color:var(--white)}
.footer-nav a{position:absolute;top:270px;font-size:15px;font-weight:700;color:var(--white);text-decoration:none}
.footer-nav i{position:absolute;top:270px;font-style:normal;font-size:15px}
.social{position:absolute;top:324px;width:24px;height:24px;border-radius:50%;background:var(--white)}
.copyright{position:absolute;left:0;top:362px;width:1200px;text-align:center;font-size:9px}
</style>
</head>
<body>
<div class="top-line"></div>

<header class="site-header">
  <div class="brand" style="left:110px;top:40px;font-size:32px"><span class="mark" style="width:34px;height:34px"></span>Cindervault</div>
  <a class="btn btn-orange" href="#contact" style="left:933px;top:29px;height:45px;font-size:14px">Contact Us<span class="dot"><svg viewBox="0 0 14 14"><path d="M3 7h8M7 3l4 4-4 4" stroke="currentColor" stroke-width="2" fill="none"/></svg></span></a>
  <nav class="main-nav">
    <a href="#" style="left:440px">Home</a>
    <a href="#about" style="left:543px">About Us</a>
    <a href="#services" style="left:669px">Services</a>
    <a href="#blog" style="left:787px">Blog</a>
    <a href="#" style="left:878px">Reviews</a>
    <a href="#news" style="left:995px">Latest News</a>
  </nav>
</header>

<section class="hero">
  <div class="hero-art" role="img" aria-label="Glowing digital security shield with a keyhole surrounded by network lines"></div>
  <h1 class="small">Welcome To</h1>
  <h1 class="big">Cindervault</h1>
  <p>Et harum quidem rerum facilis est et expedita distinctio. Nam libero tempore, cum soluta nobis est eligendi optio cumque</p>
  <a class="btn btn-white dark" href="#" style="left:110px;top:435px;width:154px">Get Started<span class="dot"><svg viewBox="0 0 14 14"><path d="M3 7h8M7 3l4 4-4 4" stroke="currentColor" stroke-width="2" fill="none"/></svg></span></a>
</section>

<a class="contact-cloud" href="#contact">
  <svg width="410" height="290" viewBox="0 0 410 290">
    <g fill="#ffffff">
      <circle cx="205" cy="110" r="112"/><circle cx="95" cy="190" r="100"/><circle cx="315" cy="190" r="100"/>
    </g>
    <g fill="#f26b3a">
      <circle cx="205" cy="112" r="96"/><circle cx="98" cy="190" r="86"/><circle cx="312" cy="190" r="86"/><rect x="98" y="150" width="214" height="126"/>
    </g>
    <g stroke="#ffffff" stroke-width="4" fill="none" stroke-linecap="round">
      <path d="M190 128a15 15 0 0 1 30 0"/><rect x="186" y="126" width="8" height="16" rx="3" fill="#fff"/><rect x="216" y="126" width="8" height="16" rx="3" fill="#fff"/><path d="M220 142q0 10-12 10"/>
    </g>
  </svg>
  <span class="label">Contact Us Now</span>
</a>

<section class="about" id="about">
  <div class="about-photo" role="img" aria-label="Photo of an analyst working at a computer in a dim office"></div>
  <h2><span>About</span> Us</h2>
  <p>At vero eos et accusamus et iusto odio dignissimos ducimus qui blanditiis praesentium voluptatum deleniti atque corrupti quos dolores et quas molestias excepturi sint occaecati cupiditate non provident, similique sunt in culpa qui officia deserunt mollitia animi, id est laborum et dolorum fuga. Et harum quidem rerum facilis est et expedita distinctio. Nam libero tempore</p>
  <a class="btn btn-orange" href="#" style="left:620px;top:1355px;width:152px">Read More<span class="dot"><svg viewBox="0 0 14 14"><path d="M3 7h8M7 3l4 4-4 4" stroke="currentColor" stroke-width="2" fill="none"/></svg></span></a>
</section>

<section class="services" id="services">
  <svg class="abs" style="left:0;top:0" width="350" height="150" viewBox="0 0 350 150"><g fill="#fff"><rect x="0" y="0" width="350" height="40"/><circle cx="40" cy="40" r="70"/><circle cx="150" cy="80" r="75"/><circle cx="265" cy="35" r="80"/></g></svg>
  <h2 class="sec-title" style="top:110px">Our Services</h2>
  <p class="sec-sub" style="top:190px">"At vero eos et accusamus et iusto odio dignissimos ducimus qui blanditiis praesentium voluptatum deleniti atque corrupti quos dolores et quas molestias excepturi sint occaecati cupiditate non provident</p>
  <article class="service-card" style="left:110px">
    <div class="thumb" role="img" aria-label="Dark screen of falling code around a padlock" style="background:linear-gradient(160deg,#1b2530,#0b1016)"></div>
    <h3>Bug Bounty</h3>
    <p>"At vero eos et accusamus et iusto odio dignissimos ducimus qui blanditiis praesentium voluptatum</p>
  </article>
  <article class="service-card featured" style="left:444px">
    <div class="thumb" role="img" aria-label="Hand touching a network of technology icons" style="background:linear-gradient(160deg,#3a4f8a,#1a2448)"></div>
    <h3>Penetration Testing</h3>
    <p>"At vero eos et accusamus et iusto odio dignissimos ducimus qui blanditiis praesentium voluptatum</p>
  </article>
  <article class="service-card" style="left:779px">
    <div class="thumb" role="img" aria-label="Engineers reviewing code on several monitors" style="background:linear-gradient(160deg,#3c6d94,#12283c)"></div>
    <h3>Code Review</h3>
    <p>"At vero eos et accusamus et iusto odio dignissimos ducimus qui blanditiis praesentium voluptatum</p>
  </article>
  <a class="btn btn-orange" href="#" style="left:190px;top:638px;width:152px;border:3px solid #fff">Read More<span class="dot"><svg viewBox="0 0 14 14"><path d="M3 7h8M7 3l4 4-4 4" stroke="currentColor" stroke-width="2" fill="none"/></svg></span></a>
  <a class="btn btn-white" href="#" style="left:524px;top:638px;width:152px">Read More<span class="dot"><svg viewBox="0 0 14 14"><path d="M3 7h8M7 3l4 4-4 4" stroke="currentColor" stroke-width="2" fill="none"/></svg></span></a>
  <a class="btn btn-orange" href="#" style="left:858px;top:638px;width:152px;border:3px solid #fff">Read More<span class="dot"><svg viewBox="0 0 14 14"><path d="M3 7h8M7 3l4 4-4 4" stroke="currentColor" stroke-width="2" fill="none"/></svg></span></a>
</section>

<section class="blog" id="blog">
  <h2 class="sec-title" style="top:2450px"><span>Latest</span> Blogs</h2>
  <p class="sec-sub" style="top:2530px;color:#666">"At vero eos et accusamus et iusto odio dignissimos ducimus qui blanditiis praesentium voluptatum deleniti atque corrupti quos dolores et quas molestias excepturi sint occaecati cupiditate non provident</p>
  <div class="blog-grid">
    <article class="blog-col" style="left:6px">
      <div class="blog-img" role="img" aria-label="Earth from space with glowing network connections" style="top:0;background:linear-gradient(150deg,#0a1626,#1d4a7a 60%,#0a1626)"></div>
      <span class="tag" style="right:0;top:0">APR 2023</span>
      <span class="notch" style="left:140px;top:192px;border-bottom:20px solid #fff"></span>
      <h3 style="top:253px">Lorem ipsum dolor sit amet, consec tetur adipiscing</h3>
      <p style="top:307px">Sed ut perspiciatis unde omnis iste natus error sit voluptatem accusantium doloremque laudantium,</p>
      <a style="top:364px">Learn More</a>
    </article>
    <article class="blog-col" style="left:329px">
      <h3 style="top:36px">Lorem ipsum dolor sit amet, consec tetur adipiscing</h3>
      <p style="top:90px">Sed ut perspiciatis unde omnis iste natus error sit voluptatem accusantium doloremque laudantium,</p>
      <a style="top:147px">Learn More</a>
      <div class="blog-img" role="img" aria-label="Developers looking at holographic data screens" style="top:200px;height:208px;background:linear-gradient(150deg,#2c6a9a,#15304e)"></div>
      <span class="notch" style="left:140px;top:200px;border-top:20px solid #fff"></span>
      <span class="tag" style="left:118px;top:374px">APR 2023</span>
    </article>
    <article class="blog-col" style="left:652px">
      <div class="blog-img" role="img" aria-label="Technician working between server racks" style="top:0;background:linear-gradient(150deg,#1a1d2a,#3a3f58 60%,#14161e)"></div>
      <span class="tag" style="right:0;top:0">APR 2023</span>
      <span class="notch" style="left:140px;top:192px;border-bottom:20px solid #fff"></span>
      <h3 style="top:253px">Lorem ipsum dolor sit amet, consec tetur adipiscing</h3>
      <p style="top:307px">Sed ut perspiciatis unde omnis iste natus error sit voluptatem accusantium doloremque laudantium,</p>
      <a style="top:364px">Learn More</a>
    </article>
  </div>
  <a class="btn btn-orange" href="#" style="left:522px;top:3106px;width:154px">View More<span class="dot"><svg viewBox="0 0 14 14"><path d="M3 7h8M7 3l4 4-4 4" stroke="currentColor" stroke-width="2" fill="none"/></svg></span></a>
</section>

<section class="touch" id="contact">
  <svg class="abs" style="left:850px;top:0" width="350" height="150" viewBox="0 0 350 150"><g fill="#fff"><rect x="0" y="0" width="350" height="40"/><circle cx="85" cy="35" r="80"/><circle cx="200" cy="80" r="75"/><circle cx="310" cy="40" r="70"/></g></svg>
  <h2 class="sec-title" style="top:122px">Get In Touch</h2>
  <p class="sec-sub" style="top:202px">"At vero eos et accusamus et iusto odio dignissimos ducimus qui blanditiis praesentium voluptatum deleniti atque corrupti quos dolores et quas molestias excepturi sint occaecati cupiditate non provident</p>
  <span class="field-label" style="left:165px;top:305px">Your Name</span>
  <div class="field" style="left:145px;top:334px;width:444px;height:52px">Alex</div>
  <span class="field-label" style="left:615px;top:305px">Last Name</span>
  <div class="field" style="left:601px;top:334px;width:452px;height:52px">Reed</div>
  <span class="field-label" style="left:165px;top:405px">Email Address</span>
  <div class="field" style="left:145px;top:435px;width:444px;height:52px">alexreed@inbox.net</div>
  <span class="field-label" style="left:615px;top:405px">Message</span>
  <div class="field area" style="left:601px;top:435px;width:452px;height:151px">Your Message Goes Here....</div>
  <span class="field-label" style="left:165px;top:505px">Phone</span>
  <div class="field" style="left:145px;top:535px;width:444px;height:52px">1 888 888 888</div>
  <a class="btn btn-white" href="#" style="left:516px;top:627px;width:165px">Submit Now<span class="dot"><svg viewBox="0 0 14 14"><path d="M3 7h8M7 3l4 4-4 4" stroke="currentColor" stroke-width="2" fill="none"/></svg></span></a>
</section>

<section class="news" id="news">
  <h2 class="sec-title" style="top:4110px"><span>Latest</span> News</h2>
  <p class="sec-sub" style="top:4188px;color:#666">"At vero eos et accusamus et iusto odio dignissimos ducimus qui blanditiis praesentium voluptatum deleniti atque corrupti quos dolores et quas molestias excepturi sint occaecati cupiditate non provident</p>
  <article class="news-card" style="left:91px">
    <div class="thumb" role="img" aria-label="Glowing padlock on a circuit board" style="background:linear-gradient(150deg,#0d2a4a,#1f6aa0 55%,#0b1a30)"></div>
    <h3>vero eos et accusamus et iusto odio dignissimos ducimus</h3>
    <p>Sed ut perspiciatis unde omnis iste natus error sit voluptatem accusantium doloremque laudantium</p>
    <div class="meta"><span>Owen Carrick</span><span>22 April 2023</span></div>
  </article>
  <article class="news-card" style="left:442px">
    <div class="thumb" role="img" aria-label="Cyber security dial surrounded by digital icons" style="background:radial-gradient(circle at 50% 50%,#3c6fd0,#10245a 70%)"></div>
    <h3>vero eos et accusamus et iusto odio dignissimos ducimus</h3>
    <p>Sed ut perspiciatis unde omnis iste natus error sit voluptatem accusantium doloremque laudantium</p>
    <div class="meta"><span>Owen Carrick</span><span>22 April 2023</span></div>
  </article>
  <article class="news-card" style="left:793px">
    <div class="thumb" role="img" aria-label="Digital padlock over a blue data grid" style="background:linear-gradient(150deg,#0a2a44,#1f7aa8 55%,#0a2238)"></div>
    <h3>vero eos et accusamus et iusto odio dignissimos ducimus</h3>
    <p>Sed ut perspiciatis unde omnis iste natus error sit voluptatem accusantium doloremque laudantium</p>
    <div class="meta"><span>Owen Carrick</span><span>22 April 2023</span></div>
  </article>
  <a class="btn btn-orange" href="#" style="left:522px;top:4743px;width:154px">View More<span class="dot"><svg viewBox="0 0 14 14"><path d="M3 7h8M7 3l4 4-4 4" stroke="currentColor" stroke-width="2" fill="none"/></svg></span></a>
</section>

<footer class="site-footer">
  <svg class="abs" style="left:0;top:0" width="350" height="170" viewBox="0 0 350 170"><g fill="#fff"><rect x="0" y="0" width="350" height="40"/><circle cx="40" cy="45" r="75"/><circle cx="150" cy="90" r="75"/><circle cx="265" cy="35" r="80"/></g></svg>
  <div class="brand" style="left:0;width:1200px;top:150px;justify-content:center;color:#fff;font-size:46px;flex-direction:column;gap:14px"><span class="mark" style="width:56px;height:56px;background:#fff"></span>Cindervault</div>
  <nav class="footer-nav">
    <a href="#" style="left:229px">Home</a><i style="left:326px">|</i>
    <a href="#about" style="left:388px">About Us</a><i style="left:508px">|</i>
    <a href="#services" style="left:569px">Services</a><i style="left:684px">|</i>
    <a href="#blog" style="left:745px">Blog</a><i style="left:832px">|</i>
    <a href="#contact" style="left:893px">Contact Us</a>
  </nav>
  <span class="social" style="left:531px" role="img" aria-label="Social profile"></span>
  <span class="social" style="left:569px" role="img" aria-label="Social profile"></span>
  <span class="social" style="left:607px" role="img" aria-label="Social profile"></span>
  <span class="social" style="left:645px" role="img" aria-label="Social profile"></span>
  <p class="copyright">© Copyright 2023 Cindervault | All Rights Reserved</p>
</footer>
</body>
</html>
```